Consultant company (start up) needs a bold, yet simple web design

We need a we design for "K7P Ledger & Consulting". As our name implies we are a consultant firm helping companies with public sector business (tenders), but also helping the buyer side. We provide market research and reports, advice (legal and business) and hands-on-help with tender applications (projectleader; analysing critiera and texts, document reviews, etc). We have a rather uniqe position in our market with our mixed competences of branding and market communication, formal management systems, and public tenders.

We have a strong drive to make tender business simple for our clients: we will take care of the complicated!

We want our web design to be bold, yet clean and simple, communicating:

Competence; Commitment, Simplicity (for the customer).
Updates

Reason: For different reasons our web project was put on hold/was delayed a few days. As of today we are kicking life into it again, and expect to come back with feedback on designs in the next days. Best regards, Mattias

Target Market(s)

We primarily help companies aiming for public contracts.

Industry/Entity Type

Business Consultant

Contact Information for Business Card

Company logo; First name, Last name, Titel, webadress; personal e-mail
Maybe: a motto like "Offentliga affärer. Enklare" ("Public business. Made simple.")

Coding

Coded - Design and coding required

Font styles to use
Sans Serif

Colors

Designer to choose colors to be used in the design.

Requirements
Must have
• Dual language (Swedish and English)
• Responsive design, many people will view our webpage on their phone or tavlo.
• We want to make our position clear, stating what distinguishes us from "the rest of the pack" in maybe with on the starting page.
• [Will update brief; need to think this through]
Nice to have
• We have our logo in three colours. Green is our first. We are not yet sure why we have the different colurs. Maybe (just maybe!) the different colours can be put to use?
• We need help with the choice of images.
Should not have
• Never boring.

```html
<!DOCTYPE html>
<html lang="en">
<head>
<meta charset="utf-8">
<title>K7P Ledger &amp; Consulting</title>
<link rel="stylesheet" href="https://fonts.googleapis.com/css2?family=Lato:wght@400;700&family=Montserrat:wght@700&display=swap">
<style>
  :root {
    --brand-blue: #3aaadc;
    --brand-ink: #1f6fb8;
    --nav-grey: #777777;
    --white: #ffffff;
    --hero-dark: #3b3b3b;
    --hero-mid: #6a6a6a;
    --hero-light: #9a9a9a;
  }
  * { box-sizing: border-box; margin: 0; padding: 0; }
  html, body { width: 1200px; height: 541px; overflow: hidden; background: var(--white); }
  body { font-family: "Lato", Arial, sans-serif; position: relative; }

  .site-header {
    position: absolute; top: 0; left: 0; width: 1200px; height: 91px;
    background: var(--white);
  }
  .brand {
    position: absolute; left: 125px; top: 27px;
    display: flex; align-items: center; gap: 10px;
    text-decoration: none;
  }
  .brand-dot { width: 30px; height: 30px; border-radius: 50%; background: var(--brand-ink); }
  .brand-name {
    font-family: "Lato", Arial, sans-serif; font-weight: 700; font-size: 19px;
    color: var(--brand-ink); letter-spacing: 0.2px; line-height: 1.1;
  }
  .main-nav {
    position: absolute; right: 118px; top: 30px;
    display: flex; align-items: center; gap: 22px;
  }
  .nav-link {
    font-weight: 700; font-size: 13px; color: var(--nav-grey);
    text-decoration: none; text-transform: uppercase; line-height: 28px;
    display: flex; align-items: center; gap: 5px; position: relative;
  }
  .nav-link.is-active { color: var(--brand-blue); }
  .nav-link.is-active::after {
    content: ""; position: absolute; left: 0; right: 0; bottom: -6px;
    height: 1px; background: var(--brand-blue);
  }
  .nav-cta {
    background: var(--brand-blue); color: var(--white);
    padding: 0 12px; border-radius: 2px; margin-left: 2px;
  }

  .hero {
    position: absolute; top: 91px; left: 0; width: 1200px; height: 450px;
    overflow: hidden; text-align: center; color: var(--white);
  }
  .hero-photo {
    position: absolute; inset: 0;
    background:
      radial-gradient(ellipse at 50% 40%, var(--hero-light) 0%, var(--hero-mid) 45%, var(--hero-dark) 100%);
  }
  .hero-shade { position: absolute; inset: 0; background: rgba(30, 30, 30, 0.45); }
  .hero-content { position: absolute; top: 0; left: 0; width: 100%; }
  .hero-kicker {
    position: absolute; top: 86px; width: 100%;
    font-family: "Montserrat", Arial, sans-serif; font-weight: 700;
    font-size: 27px; letter-spacing: 3px;
  }
  .hero-rule {
    position: absolute; top: 128px; left: 583px; width: 35px; height: 1px;
    background: var(--white);
  }
  .hero-title {
    position: absolute; top: 150px; left: 250px; width: 700px;
    font-family: "Montserrat", Arial, sans-serif; font-weight: 700;
    font-size: 53px; line-height: 53px; letter-spacing: 7px;
  }
  .hero-lede {
    position: absolute; top: 264px; left: 250px; width: 700px;
    font-size: 15px; line-height: 24px;
  }
  .hero-button {
    position: absolute; top: 330px; left: 527px; width: 148px; height: 41px;
    background: var(--brand-blue); color: var(--white); text-decoration: none;
    font-size: 18px; line-height: 41px; border-radius: 2px;
  }
  .scroll-cue { position: absolute; top: 416px; left: 594px; }
</style>
</head>
<body>
  <header class="site-header">
    <a class="brand" href="#">
      <span class="brand-dot"></span>
      <span class="brand-name">K7P Ledger &amp; Consulting</span>
    </a>
    <nav class="main-nav">
      <a class="nav-link is-active" href="#">Home</a>
      <a class="nav-link" href="#">About Us</a>
      <a class="nav-link" href="#">Services
        <svg width="9" height="6" viewBox="0 0 9 6"><path d="M1 1l3.5 3.5L8 1" fill="none" stroke="#777" stroke-width="1.4"/></svg>
      </a>
      <a class="nav-link" href="#">Blog</a>
      <a class="nav-link" href="#">Site Map</a>
      <a class="nav-link nav-cta" href="#">Contact Us</a>
    </nav>
  </header>

  <section class="hero">
    <div class="hero-photo" role="img" aria-label="Top-down photo of two colleagues working at a desk with a laptop"></div>
    <div class="hero-shade"></div>
    <div class="hero-content">
      <p class="hero-kicker">WELCOME TO</p>
      <span class="hero-rule"></span>
      <h1 class="hero-title">K7P LEDGER &amp; CONSULTING</h1>
      <p class="hero-lede">Lorem ipsum dolor sit amet, consectetur adipiscing elit, sed do eiusmod tempor incididunt ut labore et dolore magna aliqua. Ut enim ad minim veniam, quis nostrud exercitation</p>
      <a class="hero-button" href="#">LEARN MORE</a>
      <svg class="scroll-cue" width="12" height="8" viewBox="0 0 12 8"><path d="M1 1.5l5 5 5-5" fill="none" stroke="#fff" stroke-width="1.8"/></svg>
    </div>
  </section>
</body>
</html>
```